Premium Relish Company Needs Postcard size Shelf talker

Business name: Bellamy & Roo Gilded Pantry
www.bellamyandroo-pantry.com.au
Product/service/brand name:
Bellamy & Roo Gilded Pantry. We produce the MOST delicious premium relishes in Australia and they retail in all premium deli’s, butchers, and high end supermarkets in NSW and VIC. Please see our website for further details: www.bellamyandroo-pantry.com.au
Key Objective:
Design a Post card size shelf talker. These are small signs that attach to a retail shelf ledge. Shelf Talkers are an effective way to attract and communicate with customer's in-store as they are wandering the aisles. OUR key objective is to attract EVERY single potential customer to the relish and make them buy.
Marketing objectives:
Build Brand awareness, Increase sales by creating enough curiosity for a customer to purchase the product immediately without trying it. We want something that will catch the eye and increase their interest until picking up the product off the shelf and putting it in their basket seems the most logical and sensible option to them, as opposed to them feeling they are involved in a great risk.
Our Image:
We like humour and our two phrases "Chutney turned cheeky" & "Makes everything better. - EVERYTHING!" reflect this. We like to appeal to their happier side when they purchase our product.
We don't want busy imagery.
Please avoid the brash colours and imagery associated with take away food. This is premium cuisine, with a modern urban angle – but not up itself. It is the perfect accompaniment to a fantastic quality BBQ for average Australian and the perfect condiment to always keep in the fridge as it is the only condiment on the market that is FULL of REAL flavour.
Key Concepts:
FUNNY, URBAN, RELEVANT
FUNNY – Chaotic Adult fun. A strong sense of the child within.
NOT CHILDLIKE
URBAN – Stay away from the conservative “country image” that most of our competitors use. We don’t want to look like we were made out on a farm somewhere.
RELEVANT – THIS IS SOMETHING EVERYONE WILL WANT TO EAT!
It is relevant to everyone and will make everything they eat it with better. Everything.
Target Audience:
Our target audience is ANYONE who loves premium quality food and is willing to pay a little bit more for a great tasting product as opposed to settling for a cheaper relish that is below average, processed and filled with additives and nasties. Our current demographic is middle-class, comfortable income, mainly Anglo-Saxon Australians - age range is quite broad from young up to professionals to comfortably set retirees.
Non Negotiable Elements of the design: The Logo
Size: Postcard - PORTRAIT ORIENTATION
File format: Happy for you to suggest which format is best.
Stock : 350gsm paper
Colours: Dominant colour must be a “Roma Tomato” Red, however keep colours down to Maximum 4
Design:
Double sided .
Front will have writing as follows with long logo incorporated as well:
BELLAMY & ROO (LOGO)
Chutney turned cheeky (this should fit right under the logo )
• 100% Natural
• Luscious Full Flavour
• Award Winning
• Gluten Free
• Vegan Friendly
• Modern Australian Taste
.........with echoes of tradition.
Makes everything better. Everything!
Back will have burger image with short logo above it
Updates
SORRY! Forgot to mention that design layout needs to be PORTRAIT. Thanks
Reason: I have been away and need a bit more time to consider designs.

```html
<!DOCTYPE html>
<html lang="en">
<head>
<meta charset="utf-8">
<title>Bellamy &amp; Roo Gilded Pantry – Shelf Talker</title>
<link rel="stylesheet" href="https://fonts.googleapis.com/css2?family=Libre+Baskerville:wght@400;700&family=Open+Sans:wght@400&family=Special+Elite&display=swap">
<style>
  :root {
    --roma-red: #8b1e1e;
    --ink: #000000;
    --paper: #ffffff;
    --tag-ink: #000000;
    --gold: #d99a2b;
    --gold-light: #f4c85a;
    --label: #222222;
  }
  * { margin: 0; padding: 0; box-sizing: border-box; }
  html, body { width: 1200px; height: 885px; overflow: hidden; background: var(--paper); }
  body { position: relative; font-family: "Libre Baskerville", Georgia, serif; }

  .side-label {
    position: absolute; top: 28px;
    font-family: "Open Sans", Arial, sans-serif; font-size: 20px; color: var(--label);
  }
  .side-label--front { left: 12px; }
  .side-label--back { left: 607px; }

  .card { position: absolute; overflow: hidden; border: 1px solid #444; }
  .card--front { left: 10px; top: 57px; width: 586px; height: 758px; background: var(--ink); }
  .card--back { left: 604px; top: 57px; width: 578px; height: 756px; }

  .header-band { position: absolute; left: 0; top: 0; width: 586px; height: 200px; }
  .brand-name {
    position: absolute; left: 0; top: 30px; width: 586px; text-align: center;
    font-size: 62px; line-height: 76px; font-weight: 700; color: var(--paper); letter-spacing: -1px;
  }
  .tagline {
    position: absolute; left: 0; top: 126px; width: 586px; text-align: center;
    font-size: 25px; line-height: 32px; font-weight: 700; color: var(--tag-ink); text-transform: uppercase;
  }

  .benefits {
    position: absolute; left: 28px; top: 222px; list-style: none;
    color: var(--paper); font-size: 24px; font-weight: 700; line-height: 35px;
  }
  .benefits li:first-child { padding-left: 4px; }

  .promise-seal {
    position: absolute; left: 370px; top: 208px; width: 182px; height: 182px;
    border-radius: 50%; background: var(--roma-red); border: 4px solid var(--paper);
    display: flex; align-items: center; justify-content: center;
  }
  .promise-seal p {
    font-family: "Special Elite", "Courier New", monospace; color: var(--paper);
    font-size: 19px; line-height: 23px; text-align: center; transform: rotate(28deg);
  }

  .award-medal {
    position: absolute; left: 43px; top: 440px; width: 212px; height: 212px; border-radius: 50%;
    background: radial-gradient(circle at 40% 35%, var(--gold-light), var(--gold) 60%, #8a5a14);
  }

  .taste-line {
    position: absolute; left: 240px; top: 465px; width: 336px; text-align: center;
    color: var(--paper); font-size: 40px; font-weight: 700; line-height: 57px;
  }

  .footer-rule { position: absolute; left: 0; width: 586px; background: var(--paper); height: 10px; }
  .footer-rule--top { top: 661px; }
  .footer-rule--bottom { top: 725px; }
  .footer-band {
    position: absolute; left: 0; top: 671px; width: 586px; height: 54px;
    background: var(--roma-red); color: var(--paper);
    font-size: 30px; line-height: 54px; text-align: center; letter-spacing: -0.5px;
  }

  .burger-photo {
    position: absolute; inset: 0;
    background: linear-gradient(180deg, #d9b47a 0%, #c9453a 18%, #6b7a2c 30%, #7a3a5a 42%, #f0a020 58%, #4a2a18 75%, #5d8a2e 85%, #d6b486 100%);
  }
  .back-brand {
    position: absolute; left: 150px; top: 565px; width: 400px;
    font-size: 64px; font-weight: 700; line-height: 70px; color: var(--paper); text-align: center;
  }
</style>
</head>
<body>
  <span class="side-label side-label--front">Front</span>
  <span class="side-label side-label--back">Back</span>

  <section class="card card--front">
    <svg class="header-band" viewBox="0 0 586 200" aria-hidden="true">
      <path d="M0 0 H586 V138 Q293 236 0 138 Z" fill="var(--roma-red)"/>
      <path d="M0 142 Q293 240 586 142" fill="none" stroke="var(--paper)" stroke-width="5"/>
    </svg>
    <h1 class="brand-name">Bellamy &amp; Roo</h1>
    <p class="tagline">Chutney turned cheeky</p>

    <ul class="benefits">
      <li>100% Natural</li>
      <li>Luscious Full Flavour</li>
      <li>Award Winning</li>
      <li>Gluten Free</li>
      <li>Vegan Friendly</li>
    </ul>

    <div class="promise-seal"><p>Makes<br>everything<br>better.<br>Everything</p></div>

    <div class="award-medal" role="img" aria-label="Gold award medal for the relishes"></div>

    <p class="taste-line">modern<br>Austalian<br>taste</p>

    <div class="footer-rule footer-rule--top"></div>
    <p class="footer-band">www.bellamyandroo-pantry.com.au</p>
    <div class="footer-rule footer-rule--bottom"></div>
  </section>

  <section class="card card--back">
    <div class="burger-photo" role="img" aria-label="Close-up photo of a gourmet burger with pickles, red onion, melted cheese, beef patty and lettuce"></div>
    <p class="back-brand">Bellamy<br>&amp; Roo</p>
  </section>
</body>
</html>
```